PowerPoint template for large technology company

Requesting proposals for a PowerPoint deck template that can be used by our sales team when pitching clients. We are a large technology media company, that is BtoB focused, and are looking for a professional, clean, tech-forward, design and layout. However, our clients are advertisers and brands who would respond well to a subtly stylized creative design.

We need a fully built-out template wherein our sales team can choose from a variety of slide layouts while compiling their pitch decks.

Key objective: To create a template that mandates consistent fonts, sizes, and layout, and is easy to use for novice presenters. A plug-and-play template.

Secondary objective: A refresh on current design of company template.

Presentation template should include:
2 Presentation title slide options
2 Section header options
6 information layout slide options
3 data charts (pie, bar, and column)
Summary/ Thank you slide

The teams using this template will not be adept with PowerPoint but should easily be able to insert images and text boxes without it ruining the design and format of the presentation. The idea is if 20 people use our template to build pitch-decks, all of the individual decks should all look like they came from the same team. Please be as detailed and specific as possible when building out slides.

Simple, high-compatibility fonts. Please see brand guidelines attached.

Target Market(s)

Large advertising agencies and major consumer technology brands.

This deck template will not be consumer facing.

Industry/Entity Type

Building

Font styles to use
Serif
Sans Serif

Requirements
Must have
• Must be clean, high-tech, and forces user to stay within template guidelines during modifications.

Template should be built out for a sales presentation that will be a tool for ppt novices.
Nice to have
• As we are revamping existing decks, it will be nice to see multiple ideas on the design. Think professional, high-tech, and powerful.
Should not have
• Should not have a distracting background that will interfere with presentations or where it will be difficult to easily insert images.

Blacked out backgrounds cause a "boxed in" look for images and/or text boxes - which is undesirable. Either don't include color-blocked backgrounds or introduce a way in which this can be used that avoids the previously stated pitfall.

No rotated text-fill options. (i.e. rotating text by 90 or 180 degrees)

Please don't be too literal in your design approach.

```html
<!DOCTYPE html>
<html lang="en">
<head>
<meta charset="utf-8">
<title>Table – Financial Data</title>
<link href="https://fonts.googleapis.com/css2?family=Questrial&family=Roboto:wght@300;400&display=swap" rel="stylesheet">
<style>
  :root {
    --ink-slate: #3b5670;
    --brand-red: #bd0026;
    --row-grey: #9a9fa4;
    --row-light: #f1f1f1;
    --text-dark: #444a4f;
    --text-light: #ffffff;
    --frame: #111111;
    --band-pale: #eef3f8;
    --band-tint: #cfdcea;
  }
  html, body {
    margin: 0;
    padding: 0;
    overflow: hidden;
  }
  .slide {
    position: relative;
    width: 1200px;
    height: 900px;
    background: #ffffff;
    overflow: hidden;
  }
  .title-band {
    position: absolute;
    left: 0; top: 0;
    width: 1200px; height: 77px;
    background: linear-gradient(90deg, var(--band-pale) 0%, var(--band-pale) 35%, var(--band-tint) 70%, #e4ecf5 100%);
  }
  .slide-title {
    position: absolute;
    left: 44px; top: 22px;
    margin: 0;
    font-family: "Questrial", sans-serif;
    font-weight: 400;
    font-size: 25px;
    letter-spacing: 0.5px;
    color: var(--ink-slate);
  }
  .income-table {
    position: absolute;
    left: 52px; top: 147px;
    width: 1087px;
    border-collapse: collapse;
    border: 2px solid var(--frame);
    font-family: "Roboto", sans-serif;
    font-weight: 300;
    font-size: 22px;
    table-layout: fixed;
  }
  .income-table th {
    background: var(--brand-red);
    color: var(--text-light);
    font-weight: 400;
    font-size: 27px;
    text-align: left;
    height: 106px;
    padding: 0 12px;
    line-height: 1.2;
    text-shadow: 0 1px 2px rgba(0,0,0,0.35);
  }
  .income-table td {
    height: 70.6px;
    padding: 0 12px;
    white-space: nowrap;
  }
  .row-main td {
    background: var(--row-grey);
    color: var(--text-light);
    border-left: 1px solid #b6babe;
  }
  .row-main td:first-child { border-left: none; }
  .row-sub td {
    background: var(--row-light);
    color: var(--text-dark);
  }
  .row-first td {
    background: var(--row-light);
    color: var(--text-dark);
  }
  .label-indent { padding-left: 23px !important; }
  .footer-band {
    position: absolute;
    left: 0; top: 856px;
    width: 1200px; height: 44px;
    background: linear-gradient(180deg, #f3f6fa 0%, #e6edf5 100%);
  }
  .footer-note {
    position: absolute;
    left: 18px; top: 866px;
    margin: 0;
    font-family: "Questrial", sans-serif;
    font-size: 20px;
    letter-spacing: 0.6px;
    color: var(--ink-slate);
  }
</style>
</head>
<body>
<div class="slide">
  <div class="title-band" role="img" aria-label="Soft blue circuit-board line pattern fading in from the right"></div>
  <h1 class="slide-title">TABLE – FINANCIAL DATA</h1>

  <table class="income-table">
    <colgroup>
      <col style="width:336px">
      <col style="width:153px">
      <col style="width:149px">
      <col style="width:150px">
      <col style="width:150px">
      <col style="width:149px">
    </colgroup>
    <thead>
      <tr>
        <th>Projected Income<br>Statement</th>
        <th>Year 1</th>
        <th>Year 2</th>
        <th>Year 3</th>
        <th>Year 4</th>
        <th>Year 5</th>
      </tr>
    </thead>
    <tbody>
      <tr class="row-first">
        <td>Revenue</td>
        <td>$3,273,837</td>
        <td>$11,502,260</td>
        <td>$23,473,091</td>
        <td>$38,956,187</td>
        <td>$59,530,474</td>
      </tr>
      <tr class="row-main">
        <td>Cost of Goods Sold</td>
        <td>$762,714</td>
        <td>$2,711,511</td>
        <td>$5,546,648</td>
        <td>$9,213,620</td>
        <td>$14,086,374</td>
      </tr>
      <tr class="row-sub">
        <td class="label-indent">COGS percentage</td>
        <td>23%</td>
        <td>24%</td>
        <td>24%</td>
        <td>24%</td>
        <td>24%</td>
      </tr>
      <tr class="row-main">
        <td>Gross Margin</td>
        <td>$2,511,122</td>
        <td>$8,790,749</td>
        <td>$17,926,443</td>
        <td>$29,742,568</td>
        <td>$45,444,100</td>
      </tr>
      <tr class="row-sub">
        <td class="label-indent">Gross Margin percentage</td>
        <td>77%</td>
        <td>76%</td>
        <td>76%</td>
        <td>76%</td>
        <td>76%</td>
      </tr>
      <tr class="row-main">
        <td>SG&amp;A expenses</td>
        <td>$2,228,042</td>
        <td>$5,167,073</td>
        <td>$8,834,526</td>
        <td>$13,063,320</td>
        <td>$21,229,107</td>
      </tr>
      <tr class="row-sub">
        <td style="padding-left:18px">SG&amp;A percentage</td>
        <td>68%</td>
        <td>45%</td>
        <td>38%</td>
        <td>34%</td>
        <td>36%</td>
      </tr>
    </tbody>
  </table>

  <div class="footer-band" role="img" aria-label="Faint light-blue grid pattern band"></div>
  <p class="footer-note">Grid Harbor – Data Powered Media. Copyright 2013</p>
</div>
</body>
</html>
```